Law Office Business Card

We need a business card design to include the following information:
Name of Firm: Brennick Law Group, P.A.
Address: 4627 Sandlot Ave, Ste 208, Corrin Bay, FL 34990
Phone: 561-555-0148
Fax: 561-555-0193
Website: http://www.tbrennicklaw.example

We Need a place for the Person's name and email address. Please start with the following:
Lorna K. Dwyer, Esq.
lorna@tbrennicklaw.example

```html
<!DOCTYPE html>
<html lang="en">
<head>
<meta charset="utf-8">
<title>Brennick Law Group – Business Card</title>
<link rel="stylesheet" href="https://fonts.googleapis.com/css2?family=Cinzel:wght@400;500&family=Marcellus&display=swap">
<style>
  :root {
    --backdrop: #f6c47c;
    --card: #ffffff;
    --gold: #b59e78;
    --gold-dark: #9c8766;
    --band-start: #8e857d;
    --band-end: #c6b79c;
    --ink: #1d1d1d;
    --light-strip: #eeeeec;
    --rule: #c9c4bc;
  }
  * { box-sizing: border-box; margin: 0; padding: 0; }
  html, body {
    width: 1200px; height: 786px; overflow: hidden;
    background: var(--backdrop);
  }
  .card {
    position: absolute; left: 75px; top: 93px;
    width: 1050px; height: 600px;
    background: var(--card);
    box-shadow: 0 14px 40px rgba(120, 70, 10, .25);
    overflow: hidden;
    font-family: "Marcellus", "Cinzel", serif;
  }
  .brand {
    position: absolute; left: 70px; top: 56px;
    display: flex; align-items: center; gap: 18px;
  }
  .brand-square {
    width: 58px; height: 58px;
    border: 2px solid var(--gold);
  }
  .brand-name {
    font-family: "Cinzel", serif; font-weight: 400;
    color: var(--gold-dark);
    font-size: 34px; line-height: 1.05; letter-spacing: 2px;
    text-transform: uppercase;
  }
  .brand-name small { display: block; font-size: 34px; }
  .person {
    position: absolute; right: 70px; top: 190px; text-align: right;
  }
  .person-name {
    font-family: "Cinzel", serif; font-weight: 400;
    color: var(--gold); font-size: 40px; letter-spacing: 2px;
    text-transform: uppercase;
  }
  .person-email {
    margin-top: 6px;
    display: flex; align-items: center; justify-content: flex-end; gap: 12px;
    font-size: 27px; color: var(--ink); letter-spacing: 1px; text-transform: uppercase;
  }
  .band {
    position: absolute; left: 0; top: 300px; width: 100%; height: 180px;
    background: linear-gradient(90deg, var(--band-start), var(--band-end));
  }
  .contact-lines {
    position: absolute; left: 60px; top: 22px;
    color: #fff; font-size: 25px; line-height: 42px;
  }
  .contact-lines div { display: flex; align-items: center; gap: 10px; }
  .address {
    position: absolute; right: 70px; top: 60px; text-align: right;
    color: #fff; font-family: "Cinzel", serif; font-size: 33px; line-height: 46px;
    letter-spacing: 1.5px;
  }
  .rule {
    position: absolute; left: 0; top: 516px; width: 340px; height: 2px;
    background: var(--rule);
  }
  .web {
    position: absolute; right: 70px; top: 500px;
    display: flex; align-items: center; gap: 14px;
    color: var(--gold); font-family: "Cinzel", serif; font-size: 31px; letter-spacing: 1.5px;
    text-transform: uppercase;
  }
  .foot-strip {
    position: absolute; left: 0; bottom: 0; width: 100%; height: 28px;
    background: var(--light-strip);
  }
</style>
</head>
<body>
  <div class="card">
    <div class="brand">
      <div class="brand-square"></div>
      <div class="brand-name">Brennick Law<small>Group</small></div>
    </div>

    <div class="person">
      <div class="person-name">Lorna K. Dwyer, Esq.</div>
      <div class="person-email">
        <svg width="26" height="18" viewBox="0 0 26 18" aria-hidden="true">
          <rect x="1" y="1" width="24" height="16" fill="none" stroke="#1d1d1d" stroke-width="1.6"/>
          <path d="M1 1 L13 10 L25 1" fill="none" stroke="#1d1d1d" stroke-width="1.6"/>
        </svg>
        lorna@tbrennicklaw.example
      </div>
    </div>

    <div class="band">
      <div class="contact-lines">
        <div>
          <svg width="22" height="22" viewBox="0 0 22 22" aria-hidden="true">
            <circle cx="11" cy="11" r="10" fill="none" stroke="#fff" stroke-width="1.5"/>
            <path d="M7 6 q-1 5 4 9 q3 2 4 0 l-2-2 l-1 1 q-3-2 -3-5 l1-1 z" fill="#fff"/>
          </svg>
          561-555-0148
        </div>
        <div>
          <svg width="22" height="22" viewBox="0 0 22 22" aria-hidden="true">
            <circle cx="11" cy="11" r="10" fill="none" stroke="#fff" stroke-width="1.5"/>
            <rect x="6" y="9" width="10" height="6" fill="#fff"/>
            <rect x="8" y="5" width="6" height="4" fill="none" stroke="#fff" stroke-width="1.2"/>
          </svg>
          561-555-0193
        </div>
      </div>
      <div class="address">
        4627 Sandlot Ave, Ste 208<br>
        Corrin Bay, FL 34990
      </div>
    </div>

    <div class="rule"></div>
    <div class="web">
      <svg width="26" height="26" viewBox="0 0 26 26" aria-hidden="true">
        <circle cx="13" cy="13" r="11" fill="none" stroke="#b59e78" stroke-width="1.6"/>
        <ellipse cx="13" cy="13" rx="5" ry="11" fill="none" stroke="#b59e78" stroke-width="1.3"/>
        <path d="M2 13 H24 M4 7 H22 M4 19 H22" stroke="#b59e78" stroke-width="1.2"/>
      </svg>
      www.tbrennicklaw.example
    </div>
    <div class="foot-strip"></div>
  </div>
</body>
</html>
```